High Impact Sales Presentation

We need an updated powerpoint design that will be consistent with our new brand logo and website currently underdevelopment.

We are a B2B healthcare marketing firm that helps innovative healthcare companies measurably improve organic growth.

The presentation needs to be sophisticated and visually compelling.

Target Market(s)

B2B healthcare companies selling products and services to healthcare providers and payers.

Industry/Entity Type

Healthcare

Other font styles liked:
• Sans Serif...match the website

Requirements
Must have
• 1. Dramatic cover slide, table of contents and 2nd sheet (title and content)
• 2. Follow the color scheme of the logo
• 3. BLN identification on each slide
Should not have
• Clip art

```html
<!DOCTYPE html>
<html lang="en">
<head>
<meta charset="utf-8">
<title>BLN – Sales Presentation</title>
<link rel="stylesheet" href="https://fonts.googleapis.com/css2?family=Arimo:wght@400;700&display=swap">
<style>
:root{
  --navy:#1f2d6e;
  --navy-deep:#17225a;
  --slate:#4c5157;
  --grey:#8a8f96;
  --grey-light:#c9ccd1;
  --paper:#fbfbfc;
  --sky:#dfe6ee;
  --stage:#e9e9eb;
  --ink:#3a3e44;
}
*{margin:0;padding:0;box-sizing:border-box}
html,body{width:960px;height:1200px;overflow:hidden;background:var(--stage)}
body{position:relative;font-family:"Arimo",Arial,sans-serif;color:var(--ink)}
.slide{position:absolute;width:204px;height:115px;background:var(--paper);overflow:hidden;box-shadow:0 1px 4px rgba(0,0,0,.22)}
.slide.large{width:306px;height:172px}
.photo{position:absolute}
.photo.towers{background:linear-gradient(160deg,#cfdcec 0%,#6f8fb8 35%,#2d4f86 65%,#1b3260 100%)}
.photo.sky{background:linear-gradient(180deg,#c6d3e1 0%,#eef2f6 55%,#dfe6ee 100%)}
.photo.portrait{background:linear-gradient(180deg,#c9b8a6 0%,#8a6e5a 55%,#2f3440 100%)}
.brand-foot{position:absolute;left:3px;bottom:2px;font:700 5px "Arimo",sans-serif;color:var(--navy);letter-spacing:.2px;line-height:5px}
.page-dots{position:absolute;right:5px;bottom:3px;font-size:3px;color:var(--grey-light)}
.title{position:absolute;font:400 8px "Arimo",sans-serif;color:var(--slate);text-transform:uppercase;letter-spacing:.1px;white-space:nowrap}
.title b{font-weight:400;color:var(--navy)}
.sub{position:absolute;font-size:3px;color:var(--grey);white-space:nowrap}
.rule{position:absolute;height:0;border-top:.6px dotted var(--grey-light)}
.tiny{position:absolute;font-size:2.6px;line-height:3.3px;color:var(--grey)}
.label{position:absolute;font-size:3.2px;color:var(--slate);white-space:nowrap}
.tag{position:absolute;height:5px;font-size:3.2px;line-height:5px;color:#fff;padding-left:3px;white-space:nowrap}
.tag.navy{background:var(--navy)}
.tag.slate{background:var(--slate)}
svg{position:absolute;overflow:visible}
/* cover */
.cover-name{position:absolute;left:0;top:66px;width:100%;display:flex;justify-content:center;align-items:center;gap:6px;font:400 24px "Arimo",sans-serif;color:var(--navy);line-height:1}
.cover-mark{width:7px;height:7px;background:var(--navy)}
.cover-band{position:absolute;left:0;bottom:0;width:100%;height:26px;background:var(--navy)}
/* thank you */
.thanks{background:var(--navy)}
.thanks-title{position:absolute;left:18px;top:72px;font:400 19px "Arimo",sans-serif;color:#fff;letter-spacing:.3px}
.thanks-title span{color:#6f7fb0}
.thanks-ask{position:absolute;left:19px;top:101px;font-size:7px;color:#fff}
.thanks-ask span{color:#4a5a92}
.contact-list{position:absolute;left:16px;top:127px;list-style:none;font-size:4.8px;line-height:7.6px;color:#e8ebf4}
.contact-list li::before{content:"•";margin-right:3px}
</style>
</head>
<body>

<!-- Cover -->
<section class="slide large" style="left:327px;top:22px">
  <div class="photo sky" style="inset:0" role="img" aria-label="Skyscrapers seen from below against a pale sky"></div>
  <div class="cover-name"><span class="cover-mark"></span><span>BLN</span></div>
  <div class="cover-band"></div>
</section>

<!-- Profile -->
<section class="slide" style="left:263px;top:219px">
  <div class="photo towers" style="inset:0" role="img" aria-label="Glass office towers reaching into a blue sky"></div>
  <div style="position:absolute;left:0;top:27px;width:102px;height:62px;background:var(--navy);opacity:.92"></div>
  <div class="label" style="left:13px;top:58px;font-size:7px;color:#fff">PROFILE</div>
  <div class="tiny" style="left:13px;top:68px;width:82px;color:#c9d0e6">We help healthcare brands grow with clear, measured plans.</div>
</section>

<!-- Why our team -->
<section class="slide" style="left:494px;top:219px">
  <div class="title" style="left:13px;top:14px;font-size:5.5px">Why <b>our team</b></div>
  <div class="sub" style="left:13px;top:22px;font-size:2.4px">Our team and how we work</div>
  <div class="tiny" style="left:13px;top:34px;width:80px">We build growth plans with care and measure each step we take together.</div>
  <div class="tiny" style="left:13px;top:55px;width:80px">We build growth plans with care and measure each step we take together.</div>
  <div class="tiny" style="left:13px;top:76px;width:80px">We build growth plans with care and measure each step we take together.</div>
  <div class="photo towers" style="left:102px;top:0;width:102px;height:115px" role="img" aria-label="Two modern glass towers under a blue sky"></div>
  <div class="brand-foot">BLN</div>
</section>

<!-- Company profile -->
<section class="slide" style="left:263px;top:349px">
  <div class="photo towers" style="inset:0" role="img" aria-label="City skyline of glass skyscrapers"></div>
  <div style="position:absolute;left:0;top:42px;width:100%;height:32px;background:var(--navy);opacity:.9"></div>
  <div class="title" style="left:44px;top:44px;font-size:11px;color:#fff"><span style="color:#3b4a86">COMPANY</span> PROFILE</div>
  <div class="tiny" style="left:6px;top:58px;width:192px;text-align:center;color:#d6dbec">We turn insight into steady growth for healthcare firms across every market we serve.</div>
</section>

<!-- Our amazing team -->
<section class="slide" style="left:494px;top:349px">
  <div class="title" style="left:13px;top:14px;font-size:5.5px"><b>Our amazing team</b></div>
  <div class="sub" style="left:13px;top:22px;font-size:2.4px">Meet the people behind our work</div>
  <div class="photo portrait" style="left:21px;top:37px;width:32px;height:34px" role="img" aria-label="Portrait photo of a team member"></div>
  <div class="photo portrait" style="left:64px;top:37px;width:32px;height:34px" role="img" aria-label="Portrait photo of a team member"></div>
  <div class="photo portrait" style="left:107px;top:37px;width:32px;height:34px" role="img" aria-label="Portrait photo of a team member"></div>
  <div class="photo portrait" style="left:150px;top:37px;width:32px;height:34px" role="img" aria-label="Portrait photo of a team member"></div>
  <div class="label" style="left:21px;top:75px;font-size:2.6px;font-weight:700">ANA REYES</div>
  <div class="label" style="left:64px;top:75px;font-size:2.6px;font-weight:700">OMAR VANCE</div>
  <div class="label" style="left:107px;top:75px;font-size:2.6px;font-weight:700">LENA PARK</div>
  <div class="label" style="left:150px;top:75px;font-size:2.6px;font-weight:700">IVY MOSS</div>
  <div class="tiny" style="left:21px;top:79px;font-size:2px">Creative Lead</div>
  <div class="tiny" style="left:64px;top:79px;font-size:2px">Sales Manager</div>
  <div class="tiny" style="left:107px;top:79px;font-size:2px">Product Lead</div>
  <div class="tiny" style="left:150px;top:79px;font-size:2px">Design Lead</div>
  <div class="tiny" style="left:21px;top:87px;font-size:2px">ana@bln.example</div>
  <div class="tiny" style="left:64px;top:87px;font-size:2px">omar@bln.example</div>
  <div class="tiny" style="left:107px;top:87px;font-size:2px">lena@bln.example</div>
  <div class="tiny" style="left:150px;top:87px;font-size:2px">ivy@bln.example</div>
  <div class="page-dots">● ○○</div>
  <div class="brand-foot">BLN</div>
</section>

<!-- Today's topics -->
<section class="slide" style="left:263px;top:478px">
  <div class="title" style="left:50px;top:6px">Today's <b>topics</b></div>
  <div class="sub" style="left:50px;top:15px">Agenda for the day ahead</div>
  <div class="rule" style="left:50px;top:20px;width:145px"></div>
  <svg width="204" height="115" style="left:0;top:0">
    <circle cx="22" cy="54" r="8.5" fill="#4c5157"/>
    <circle cx="59" cy="45" r="8.5" fill="#1f2d6e"/>
    <circle cx="96" cy="62" r="8.5" fill="#8a8f96"/>
    <circle cx="136" cy="53" r="8.5" fill="#5f646b"/>
    <circle cx="175" cy="42" r="8.5" fill="#9ea3aa"/>
    <g font-size="3.4" fill="#fff" text-anchor="middle" font-family="Arimo,sans-serif">
      <text x="22" y="55.2">11:00am</text><text x="59" y="46.2">12:00am</text><text x="96" y="63.2">1:30pm</text><text x="136" y="54.2">3:00pm</text><text x="175" y="43.2">4:00pm</text>
    </g>
  </svg>
  <div class="label" style="left:6px;top:67px">HELLO!</div>
  <div class="tiny" style="left:6px;top:71px;width:30px">Short note on this item.</div>
  <div class="label" style="left:43px;top:58px">BUSINESS</div>
  <div class="tiny" style="left:43px;top:62px;width:30px">Short note on this item.</div>
  <div class="label" style="left:80px;top:75px">LUNCH TIME</div>
  <div class="tiny" style="left:80px;top:79px;width:30px">Short note on this item.</div>
  <div class="label" style="left:120px;top:66px">MARKETING R&amp;D</div>
  <div class="tiny" style="left:120px;top:70px;width:30px">Short note on this item.</div>
  <div class="label" style="left:159px;top:55px">Q&amp;A</div>
  <div class="tiny" style="left:159px;top:59px;width:30px">Short note on this item.</div>
  <div class="page-dots">● ○○</div>
  <div class="brand-foot">BLN</div>
</section>

<!-- Key points -->
<section class="slide" style="left:494px;top:478px">
  <svg width="204" height="115" style="left:0;top:0">
    <polygon points="0,0 10,0 0,22" fill="#8a8f96"/>
    <polygon points="14,0 26,0 8,26 0,26 0,22" fill="#1f2d6e"/>
    <polygon points="204,96 204,115 190,115" fill="#1f2d6e"/>
    <polygon points="204,80 204,88 186,115 180,115" fill="#8a8f96"/>
  </svg>
  <div class="title" style="left:50px;top:6px"><b>Key points</b></div>
  <div class="sub" style="left:50px;top:15px">Although moreover mistaken kindness me</div>
  <div class="rule" style="left:50px;top:20px;width:145px"></div>
  <svg width="204" height="115" style="left:0;top:0">
    <g font-size="4" fill="#fff" text-anchor="middle" font-family="Arimo,sans-serif">
      <circle cx="26" cy="41" r="6" fill="#3a3e44"/><text x="26" y="42.4">1</text>
      <circle cx="26" cy="64" r="6" fill="#4c5157"/><text x="26" y="65.4">2</text>
      <circle cx="26" cy="87" r="6" fill="#1f2d6e"/><text x="26" y="88.4">3</text>
      <circle cx="113" cy="41" r="6" fill="#3d58b4"/><text x="113" y="42.4">4</text>
      <circle cx="113" cy="64" r="6" fill="#5f646b"/><text x="113" y="65.4">5</text>
      <circle cx="113" cy="87" r="6" fill="#b3b7bd"/><text x="113" y="88.4">6</text>
    </g>
  </svg>
  <div class="label" style="left:37px;top:35px">• Inermis hendrerit vel cu</div>
  <div class="tiny" style="left:40px;top:39px;width:58px">Brief note on this point.</div>
  <div class="label" style="left:37px;top:58px">• Id mei nibh posse copiosae</div>
  <div class="tiny" style="left:40px;top:62px;width:58px">Brief note on this point.</div>
  <div class="label" style="left:37px;top:81px;color:var(--navy)">• Cu pri nostrum accusamus</div>
  <div class="tiny" style="left:40px;top:85px;width:58px">Brief note on this point.</div>
  <div class="label" style="left:124px;top:35px;color:#6b84c9">• Cu pri nostrum accusamus</div>
  <div class="tiny" style="left:127px;top:39px;width:58px">Brief note on this point.</div>
  <div class="label" style="left:124px;top:58px">• Inermis hendrerit vel cu</div>
  <div class="tiny" style="left:127px;top:62px;width:58px">Brief note on this point.</div>
  <div class="label" style="left:124px;top:81px">• Id mei nibh posse copiosae</div>
  <div class="tiny" style="left:127px;top:85px;width:58px">Brief note on this point.</div>
  <div class="brand-foot">BLN</div>
</section>

<!-- Our promises -->
<section class="slide" style="left:263px;top:608px">
  <div class="title" style="left:13px;top:10px"><b>Our promises</b></div>
  <div class="sub" style="left:13px;top:19px">Lorem ipsum dolor sit amet, alii aliquip ei vel</div>
  <div class="label" style="left:83px;top:32px;width:40px;text-align:center;font-size:3px;white-space:normal;line-height:3.6px">We must have an answer to help you</div>
  <svg width="204" height="115" style="left:0;top:0">
    <circle cx="104" cy="58" r="10" fill="#4c5157"/>
    <circle cx="86" cy="86" r="10" fill="#1f2d6e"/>
    <circle cx="121" cy="86" r="10" fill="#8a8f96"/>
    <g font-size="2.8" fill="#fff" text-anchor="middle" font-family="Arimo,sans-serif">
      <text x="104" y="59">Solution</text><text x="86" y="87">Social</text><text x="121" y="87">Satisfaction</text>
    </g>
  </svg>
  <div class="label" style="left:13px;top:85px;font-size:3px">Connect emotionally with people</div>
  <div class="label" style="left:140px;top:86px;font-size:3px">Always think about customers</div>
  <div class="page-dots">● ○○</div>
  <div class="brand-foot">BLN</div>
</section>

<!-- Our commitment -->
<section class="slide" style="left:494px;top:608px">
  <div class="title" style="left:50px;top:6px">Our <b>commitment</b></div>
  <div class="sub" style="left:50px;top:15px">how principles discovered off increasing how reasonably</div>
  <div class="rule" style="left:50px;top:20px;width:145px"></div>
  <div class="tag slate" style="left:13px;top:31px;width:75px">• OUR <span style="color:#7f8fc4">COMMITMENT</span></div>
  <div class="tiny" style="left:18px;top:38px;width:130px">We keep our word and report results openly each month.</div>
  <div class="tag navy" style="left:40px;top:59px;width:92px">• OUR</div>
  <div class="tiny" style="left:45px;top:66px;width:130px">We keep our word and report results openly each month.</div>
  <div class="tag slate" style="left:66px;top:87px;width:68px">• OUR COMMITMENT</div>
  <div class="tiny" style="left:71px;top:94px;width:120px">We keep our word and report results openly each month.</div>
  <div class="page-dots">● ○○</div>
  <div class="brand-foot">BLN</div>
</section>

<!-- Some points for a good meeting -->
<section class="slide" style="left:263px;top:738px">
  <div class="title" style="left:50px;top:6px;font-size:6.5px">Some points for <b>a good meeting</b></div>
  <div class="sub" style="left:50px;top:14px">Ignorant saw her her drawings marriage laughter</div>
  <div class="rule" style="left:50px;top:19px;width:145px"></div>
  <div class="tag slate" style="left:16px;top:34px;width:43px">• Perhaps far</div>
  <div style="position:absolute;left:28px;top:39.5px;width:98px;height:4px;background:#7a7f86;font-size:2.4px;line-height:4px;color:#e3e5e8;padding-left:3px;white-space:nowrap">Ignorant saw her her drawings marriage laughter</div>
  <div class="tiny" style="left:18px;top:46px;width:176px">We keep our word and report results openly each month.</div>
  <div class="tag navy" style="left:16px;top:67px;width:50px">• Picture removal</div>
  <div style="position:absolute;left:28px;top:72.5px;width:98px;height:4px;background:#7a7f86;font-size:2.4px;line-height:4px;color:#e3e5e8;padding-left:3px;white-space:nowrap">Ignorant saw her her drawings marriage laughter</div>
  <div class="tiny" style="left:18px;top:79px;width:176px">We keep our word and report results openly each month.</div>
  <div class="page-dots">● ○○</div>
  <div class="brand-foot">BLN</div>
</section>

<!-- Company report charts -->
<section class="slide" style="left:494px;top:738px">
  <div class="title" style="left:13px;top:14px;font-size:6px">Company report charts</div>
  <div class="sub" style="left:13px;top:22px;font-size:2.4px">Results by month</div>
  <svg width="204" height="115" style="left:0;top:0">
    <g stroke="#e1e3e6" stroke-width=".3">
      <line x1="22" y1="40" x2="100" y2="40"/><line x1="22" y1="50" x2="100" y2="50"/><line x1="22" y1="60" x2="100" y2="60"/><line x1="22" y1="70" x2="100" y2="70"/>
      <line x1="120" y1="40" x2="198" y2="40"/><line x1="120" y1="50" x2="198" y2="50"/><line x1="120" y1="60" x2="198" y2="60"/><line x1="120" y1="70" x2="198" y2="70"/>
    </g>
    <g>
      <rect x="26" y="69" width="6" height="9" fill="#3a3e44"/><rect x="38" y="66" width="6" height="12" fill="#1f2d6e"/><rect x="50" y="64" width="6" height="14" fill="#8a8f96"/><rect x="62" y="61" width="6" height="17" fill="#4c5157"/><rect x="74" y="56" width="6" height="22" fill="#b3b7bd"/><rect x="86" y="49" width="6" height="29" fill="#1f2d6e"/>
      <rect x="124" y="72" width="6" height="6" fill="#3a3e44"/><rect x="136" y="70" width="6" height="8" fill="#1f2d6e"/><rect x="148" y="67" width="6" height="11" fill="#8a8f96"/><rect x="160" y="64" width="6" height="14" fill="#4c5157"/><rect x="172" y="60" width="6" height="18" fill="#b3b7bd"/><rect x="184" y="46" width="6" height="32" fill="#1f2d6e"/>
    </g>
    <line x1="22" y1="78" x2="100" y2="78" stroke="#8a8f96" stroke-width=".4"/>
    <line x1="120" y1="78" x2="198" y2="78" stroke="#8a8f96" stroke-width=".4"/>
    <circle cx="110" cy="64" r="5" fill="#3a3e44"/>
    <text x="110" y="65.5" font-size="4" fill="#fff" text-anchor="middle" font-family="Arimo,sans-serif">VS</text>
    <g font-size="2.2" fill="#4c5157" font-family="Arimo,sans-serif" text-anchor="middle">
      <text x="29" y="67">980</text><text x="41" y="64">1100</text><text x="53" y="62">1800</text><text x="65" y="59">2200</text><text x="77" y="54">3300</text><text x="89" y="47">4700</text>
      <text x="127" y="70">700</text><text x="139" y="68">1100</text><text x="151" y="65">1500</text><text x="163" y="62">2000</text><text x="175" y="58">2400</text><text x="187" y="44">5300</text>
    </g>
    <g font-size="2" fill="#8a8f96" font-family="Arimo,sans-serif" text-anchor="middle">
      <text x="29" y="81">January</text><text x="41" y="81">February</text><text x="53" y="81">March</text><text x="65" y="81">April</text><text x="77" y="81">May</text><text x="89" y="81">June</text>
      <text x="127" y="81">January</text><text x="139" y="81">February</text><text x="151" y="81">March</text><text x="163" y="81">April</text><text x="175" y="81">May</text><text x="187" y="81">June</text>
    </g>
  </svg>
  <div class="label" style="left:52px;top:85px;font-size:2.6px;font-weight:700">REPORT 2013</div>
  <div class="tiny" style="left:22px;top:89px;width:78px;text-align:center">Summary of the year.</div>
  <div class="label" style="left:150px;top:85px;font-size:2.6px;font-weight:700">REPORT 2014</div>
  <div class="tiny" style="left:120px;top:89px;width:78px;text-align:center">Summary of the year.</div>
  <div class="page-dots">● ○○</div>
  <div class="brand-foot">BLN</div>
</section>

<!-- Sales chart -->
<section class="slide" style="left:263px;top:867px">
  <div class="title" style="left:50px;top:6px">Sales <b>chart</b></div>
  <div class="sub" style="left:50px;top:15px">Lorem ipsum dolor sit amet, alii aliquip ei vel</div>
  <div class="rule" style="left:50px;top:20px;width:145px"></div>
  <svg width="204" height="115" style="left:0;top:0">
    <g stroke="#e1e3e6" stroke-width=".3">
      <line x1="18" y1="34" x2="180" y2="34"/><line x1="18" y1="42" x2="180" y2="42"/><line x1="18" y1="50" x2="180" y2="50"/><line x1="18" y1="58" x2="180" y2="58"/><line x1="18" y1="66" x2="180" y2="66"/>
    </g>
    <g fill="#1f2d6e">
      <rect x="21" y="50" width="2.5" height="24"/><rect x="34" y="44" width="2.5" height="30"/><rect x="48" y="52" width="2.5" height="22"/><rect x="61" y="46" width="2.5" height="28"/><rect x="75" y="55" width="2.5" height="19"/><rect x="88" y="49" width="2.5" height="25"/><rect x="102" y="39" width="2.5" height="35"/><rect x="115" y="53" width="2.5" height="21"/><rect x="129" y="45" width="2.5" height="29"/><rect x="142" y="56" width="2.5" height="18"/><rect x="156" y="48" width="2.5" height="26"/><rect x="169" y="43" width="2.5" height="31"/>
    </g>
    <g fill="#4c5157">
      <rect x="24" y="56" width="2.5" height="18"/><rect x="37" y="52" width="2.5" height="22"/><rect x="51" y="58" width="2.5" height="16"/><rect x="64" y="54" width="2.5" height="20"/><rect x="78" y="60" width="2.5" height="14"/><rect x="91" y="56" width="2.5" height="18"/><rect x="105" y="48" width="2.5" height="26"/><rect x="118" y="59" width="2.5" height="15"/><rect x="132" y="52" width="2.5" height="22"/><rect x="145" y="61" width="2.5" height="13"/><rect x="159" y="55" width="2.5" height="19"/><rect x="172" y="50" width="2.5" height="24"/>
    </g>
    <g fill="#9ea3aa">
      <rect x="27" y="60" width="2.5" height="14"/><rect x="40" y="58" width="2.5" height="16"/><rect x="54" y="62" width="2.5" height="12"/><rect x="67" y="59" width="2.5" height="15"/><rect x="81" y="63" width="2.5" height="11"/><rect x="94" y="61" width="2.5" height="13"/><rect x="108" y="55" width="2.5" height="19"/><rect x="121" y="63" width="2.5" height="11"/><rect x="135" y="58" width="2.5" height="16"/><rect x="148" y="64" width="2.5" height="10"/><rect x="162" y="60" width="2.5" height="14"/><rect x="175" y="57" width="2.5" height="17"/>
    </g>
    <polyline points="25,48 38,42 52,50 65,44 79,52 92,46 106,38 119,50 133,43 146,53 160,45 173,40" fill="none" stroke="#b3b7bd" stroke-width=".9"/>
    <g fill="#fff" stroke="#8a8f96" stroke-width=".5">
      <circle cx="25" cy="48" r="1"/><circle cx="38" cy="42" r="1"/><circle cx="52" cy="50" r="1"/><circle cx="65" cy="44" r="1"/><circle cx="79" cy="52" r="1"/><circle cx="92" cy="46" r="1"/><circle cx="106" cy="38" r="1"/><circle cx="119" cy="50" r="1"/><circle cx="133" cy="43" r="1"/><circle cx="146" cy="53" r="1"/><circle cx="160" cy="45" r="1"/><circle cx="173" cy="40" r="1"/>
    </g>
    <line x1="18" y1="74" x2="180" y2="74" stroke="#8a8f96" stroke-width=".4"/>
    <g font-size="2.4" fill="#8a8f96" font-family="Arimo,sans-serif">
      <text x="6" y="35">1500</text><text x="7" y="43">800</text><text x="7" y="51">600</text><text x="7" y="59">400</text><text x="7" y="67">200</text><text x="9" y="75">0</text>
      <text x="184" y="35">20000</text><text x="184" y="43">15000</text><text x="184" y="51">10000</text><text x="184" y="59">5000</text><text x="184" y="75">0</text>
      <text x="23" y="79">Jan</text><text x="36" y="79">Feb</text><text x="50" y="79">Mar</text><text x="63" y="79">Apr</text><text x="77" y="79">May</text><text x="90" y="79">Jun</text><text x="104" y="79">Jul</text><text x="117" y="79">Aug</text><text x="131" y="79">Sep</text><text x="144" y="79">Oct</text><text x="158" y="79">Nov</text><text x="171" y="79">Dec</text>
    </g>
  </svg>
  <div class="tag slate" style="left:17px;top:86px;width:54px">• Next Target Month: April</div>
  <div class="tiny" style="left:19px;top:93px;width:170px">Sales rose through spring and we aim to pass that mark.</div>
  <div class="page-dots">● ○○</div>
  <div class="brand-foot">BLN</div>
</section>

<!-- Positive or negative -->
<section class="slide" style="left:494px;top:867px">
  <div class="title" style="left:13px;top:11px;font-size:7px">Positive or <b>negative?</b></div>
  <div class="sub" style="left:13px;top:19px">Ignorant saw her her drawings marriage laughter</div>
  <svg width="204" height="115" style="left:0;top:0">
    <g fill="none" stroke-width="7">
      <circle cx="42" cy="55" r="16" stroke="#1f2d6e"/>
      <circle cx="42" cy="55" r="16" stroke="#8a8f96" stroke-dasharray="35 100.5" transform="rotate(-90 42 55)"/>
      <circle cx="102" cy="55" r="16" stroke="#1f2d6e"/>
      <circle cx="102" cy="55" r="16" stroke="#b3b7bd" stroke-dasharray="5 100.5" transform="rotate(-90 102 55)"/>
      <circle cx="163" cy="55" r="16" stroke="#1f2d6e"/>
      <circle cx="163" cy="55" r="16" stroke="#c9ccd1" stroke-dasharray="9 100.5" transform="rotate(-90 163 55)"/>
    </g>
    <g font-size="2.4" fill="#fff" font-family="Arimo,sans-serif">
      <text x="32" y="46">35%</text><text x="103" y="41">5%</text><text x="166" y="42">9%</text>
    </g>
  </svg>
  <div class="label" style="left:26px;top:78px;font-size:3px;color:#5f76c0">HELLO!</div>
  <div class="tiny" style="left:26px;top:82px;width:34px">Short note here.</div>
  <div class="label" style="left:86px;top:78px;font-size:3px;color:#5f76c0">HELLO!</div>
  <div class="tiny" style="left:86px;top:82px;width:34px">Short note here.</div>
  <div class="label" style="left:147px;top:78px;font-size:3px;color:#5f76c0">HELLO!</div>
  <div class="tiny" style="left:147px;top:82px;width:34px">Short note here.</div>
  <div class="page-dots">● ○○</div>
  <div class="brand-foot">BLN</div>
</section>

<!-- Thank you -->
<section class="slide large thanks" style="left:327px;top:1010px">
  <div class="photo towers" style="inset:0;opacity:.35" role="img" aria-label="Skyscrapers seen from below, tinted navy"></div>
  <div class="thanks-title">THANK <span>YOU!</span></div>
  <div class="thanks-ask">ANY <span>QUESTIONS?</span></div>
  <ul class="contact-list">
    <li>social.example/bln</li>
    <li>@blnpartners</li>
    <li>hello@bln-partners.example</li>
    <li>+00 555 0100 0199</li>
  </ul>
</section>

</body>
</html>
```